Pemberton Dialworks Business Card Design

Double Sided Business Card Design for a Locksmith company specializing in Safecracking, safe & vault service.

```html
<!DOCTYPE html>
<html lang="en">
<head>
<meta charset="utf-8">
<title>Pemberton Dialworks Business Card</title>
<link rel="stylesheet" href="https://fonts.googleapis.com/css2?family=Archivo+Black&family=Archivo:wght@400;600&display=swap">
<style>
  :root {
    --brand-green: #1b7a2f;
    --ink: #1c1c1c;
    --card: #f6f6f4;
    --backdrop: #e4e4e2;
    --faint: #e3e3e1;
  }
  * { margin: 0; padding: 0; box-sizing: border-box; }
  html, body { width: 1200px; height: 900px; overflow: hidden; }
  body {
    background: var(--backdrop);
    position: relative;
    font-family: "Archivo", Arial, sans-serif;
    color: var(--ink);
  }
  .card {
    position: absolute;
    width: 600px;
    height: 343px;
    background: var(--card);
    overflow: hidden;
    box-shadow: 0 6px 18px rgba(0,0,0,0.12);
  }
  /* Front: logo side */
  .card--front { left: 540px; top: 70px; }
  .front-brand {
    position: absolute;
    left: 70px;
    top: 120px;
    display: flex;
    align-items: center;
    gap: 28px;
  }
  .brand-name {
    font-family: "Archivo Black", "Arial Black", sans-serif;
    color: var(--brand-green);
    text-transform: uppercase;
    line-height: 0.95;
    letter-spacing: 1px;
  }
  .front-brand .brand-name { font-size: 44px; }
  .brand-dot {
    width: 88px; height: 88px;
    border-radius: 50%;
    background: var(--brand-green);
    flex: none;
  }
  /* Back: contact side */
  .card--back { left: 60px; top: 490px; }
  .back-brand {
    position: absolute;
    left: 34px; top: 30px;
    display: flex; align-items: center; gap: 14px;
  }
  .back-brand .brand-dot { width: 52px; height: 52px; }
  .back-brand .brand-name { font-size: 26px; }
  .faint-disc {
    position: absolute;
    right: 80px; top: 60px;
    width: 230px; height: 230px;
    border-radius: 50%;
    background: var(--faint);
  }
  .person { position: absolute; left: 34px; top: 118px; }
  .person__name {
    font-family: "Archivo Black", "Arial Black", sans-serif;
    color: var(--brand-green);
    font-size: 17px;
    letter-spacing: 0.5px;
  }
  .person__role { font-size: 12px; font-weight: 600; letter-spacing: 0.5px; margin-top: 2px; }
  .contacts { list-style: none; margin-top: 14px; font-size: 14px; }
  .contacts li { display: flex; align-items: center; gap: 8px; margin-bottom: 5px; }
  .contacts svg { width: 14px; height: 14px; flex: none; }
  .address {
    position: absolute;
    right: 36px; bottom: 44px;
    font-size: 14px; line-height: 1.35;
    text-align: left;
  }
  .address__web { color: var(--brand-green); font-weight: 600; }
  .band {
    position: absolute; left: 0; right: 0; bottom: 0;
    height: 16px; background: var(--brand-green);
  }
</style>
</head>
<body>
  <section class="card card--front" aria-label="Card front">
    <div class="front-brand">
      <div class="brand-name">Pemberton<br>Dialworks</div>
      <span class="brand-dot"></span>
    </div>
  </section>

  <section class="card card--back" aria-label="Card back">
    <div class="faint-disc"></div>
    <div class="back-brand">
      <span class="brand-dot"></span>
      <div class="brand-name">Pemberton<br>Dialworks</div>
    </div>
    <div class="person">
      <div class="person__name">MARCUS HOLLOWAY</div>
      <div class="person__role">MANAGING DIRECTOR</div>
      <ul class="contacts">
        <li><svg viewBox="0 0 14 14"><circle cx="7" cy="7" r="7" fill="var(--brand-green)"/><rect x="4.5" y="3" width="5" height="8" rx="1" fill="#fff"/></svg>555 210 34 76</li>
        <li><svg viewBox="0 0 14 14"><circle cx="7" cy="7" r="7" fill="var(--brand-green)"/><path d="M4 5.5h6v3H4z" fill="#fff"/></svg>888 402 19 63</li>
        <li><svg viewBox="0 0 14 14"><circle cx="7" cy="7" r="7" fill="var(--brand-green)"/><path d="M3.5 4.5h7v5h-7z M3.5 4.5l3.5 3 3.5-3" fill="none" stroke="#fff" stroke-width="1"/></svg>m.holloway@pembertondial.com</li>
      </ul>
    </div>
    <div class="address">
      48 Sample Lane<br>
      Fairview, Ohio 45678<br>
      <span class="address__web">www.pembertondial.com</span>
    </div>
    <div class="band"></div>
  </section>
</body>
</html>
```